Need Business Card for our Real Estate Business with Sales Executive's Picture

PANTONE 484 C ( RED)

PANTONE 2766 C ( BLUE

Industry/Entity Type

Real Estate

Contact Information for Business Card

Name, Mobile, email, & picture of Person
Agency Phone, address, Web address

Requirements
Must have
• Our Logo Colours, Agent Picture,

```html
<!DOCTYPE html>
<html lang="en">
<head>
<meta charset="utf-8">
<title>Meridian Real Estate – Business Card</title>
<link rel="stylesheet" href="https://fonts.googleapis.com/css2?family=Open+Sans:wght@400;600;700&display=swap">
<style>
  :root {
    --navy: #221a5e;
    --red: #9a3324;
    --white: #ffffff;
    --paper: #f7f7f9;
    --stage: #e6e6ea;
    --ink-blue: #2a2466;
  }
  * { box-sizing: border-box; margin: 0; padding: 0; }
  html, body { width: 1200px; height: 900px; overflow: hidden; }
  body {
    background: var(--stage);
    font-family: "Open Sans", Arial, sans-serif;
    position: relative;
  }
  .card {
    position: absolute;
    left: 250px;
    width: 700px;
    height: 400px;
    border-radius: 26px;
    overflow: hidden;
    box-shadow: 0 8px 24px rgba(0,0,0,.18);
  }
  /* Back side */
  .card-back {
    top: 35px;
    background: var(--navy);
    color: var(--white);
    text-align: center;
  }
  .card-back .brand {
    position: absolute;
    top: 130px; left: 0; right: 0;
  }
  .brand-name {
    font-weight: 600;
    letter-spacing: 4px;
    text-transform: uppercase;
  }
  .card-back .brand-name { font-size: 46px; color: var(--white); }
  .card-back .brand-sub { font-size: 15px; letter-spacing: 5px; color: var(--white); margin-top: 4px; text-transform: uppercase; }
  .card-back .web {
    position: absolute; top: 300px; left: 0; right: 0;
    font-size: 17px; color: var(--white);
  }
  .web .prefix { color: var(--red); }

  /* Front side */
  .card-front {
    top: 465px;
    background: linear-gradient(180deg, var(--white), var(--paper));
  }
  .card-front .brand { position: absolute; top: 58px; left: 50px; }
  .card-front .brand-name { font-size: 40px; color: var(--navy); }
  .card-front .brand-sub { font-size: 13px; letter-spacing: 5px; color: var(--navy); margin-top: 2px; text-transform: uppercase; }
  .person { position: absolute; top: 168px; left: 70px; }
  .person-name { font-size: 24px; font-weight: 700; color: var(--red); text-transform: uppercase; }
  .person-title { font-size: 17px; color: var(--ink-blue); text-transform: uppercase; margin-top: 2px; }
  .contacts { position: absolute; top: 240px; left: 70px; list-style: none; }
  .contacts li {
    display: flex; align-items: center; gap: 10px;
    font-size: 17px; color: var(--ink-blue); line-height: 27px;
  }
  .contacts svg { width: 18px; height: 18px; flex: none; }
  .agent-photo {
    position: absolute; top: 26px; right: 50px;
    width: 230px; height: 320px;
    background: linear-gradient(180deg, #dfe3ee 0%, #3550a0 45%, #223a86 100%);
    border-radius: 4px 4px 0 0;
  }
  .address-band {
    position: absolute; left: 0; right: 0; bottom: 0;
    height: 56px; background: var(--red);
    color: var(--white); font-size: 17px;
    display: flex; align-items: center; padding-left: 70px;
  }
</style>
</head>
<body>
  <section class="card card-back">
    <div class="brand">
      <div class="brand-name">Meridian</div>
      <div class="brand-sub">Real Estate</div>
    </div>
    <div class="web"><span class="prefix">www.</span>MeridianRealty<span class="prefix">.com</span></div>
  </section>

  <section class="card card-front">
    <div class="brand">
      <div class="brand-name">Meridian</div>
      <div class="brand-sub">Real Estate</div>
    </div>

    <div class="person">
      <div class="person-name">Daniel Hartwell</div>
      <div class="person-title">Managing Director</div>
    </div>

    <ul class="contacts">
      <li>
        <svg viewBox="0 0 20 20"><circle cx="10" cy="10" r="8.5" fill="none" stroke="var(--red)" stroke-width="1.5"/><path d="M7 6l2 2-1 1.2a6 6 0 0 0 3 3L12 11l2 2-1.2 1.2C9.5 14 6 10.5 5.8 7.2z" fill="var(--red)"/></svg>
        5550 123 456
      </li>
      <li>
        <svg viewBox="0 0 20 20"><circle cx="10" cy="10" r="8.5" fill="none" stroke="var(--red)" stroke-width="1.5"/><rect x="7" y="5" width="6" height="10" rx="1" fill="none" stroke="var(--red)" stroke-width="1.4"/><circle cx="10" cy="13" r=".8" fill="var(--red)"/></svg>
        8880 246 810
      </li>
      <li>
        <svg viewBox="0 0 20 20"><circle cx="10" cy="10" r="8.5" fill="none" stroke="var(--red)" stroke-width="1.5"/><rect x="5.5" y="7" width="9" height="6.5" fill="var(--red)"/><path d="M5.5 7l4.5 3.5L14.5 7" fill="none" stroke="var(--white)" stroke-width="1"/></svg>
        d.hartwell@meridianrealty.com
      </li>
    </ul>

    <div class="agent-photo" role="img" aria-label="Portrait photo of the agent in a blue suit"></div>

    <div class="address-band">48 Harbor Lane, Brookfield, New York 12508</div>
  </section>
</body>
</html>
```